We have logo already. Would like a modern design with white, black and orange colours. The logo can be 3D on the back of the card.
Details to go on card:
TRK Civil
Oliver Brantley - Director
17 Wexcombe Rd Tarlow NSW 2291
trkcivilworks@[url removed, login to view]
0461730582
ABN: 52 308 917 465

```html
<!DOCTYPE html>
<html lang="en">
<head>
<meta charset="utf-8">
<title>TRK Civil – Business Card</title>
<link href="https://fonts.googleapis.com/css2?family=Roboto:wght@400;500;700;900&display=swap" rel="stylesheet">
<style>
  :root {
    --navy: #1f2533;
    --navy-deep: #171c27;
    --orange: #ff5a0a;
    --white: #ffffff;
    --paper: #f4f4f6;
    --ink: #1b1e25;
    --stage: #e6e7ea;
  }
  * { box-sizing: border-box; margin: 0; padding: 0; }
  html, body { width: 1200px; height: 800px; overflow: hidden; }
  body {
    background: var(--stage);
    font-family: "Roboto", Arial, sans-serif;
    color: var(--ink);
    display: flex;
    align-items: center;
    justify-content: center;
    gap: 40px;
  }
  .card {
    position: relative;
    width: 540px;
    height: 309px;
    background: var(--white);
    overflow: hidden;
    box-shadow: 0 8px 24px rgba(0,0,0,.18);
  }

  /* Front */
  .front .dark-field {
    position: absolute; left: 0; top: 0; width: 100%; height: 172px;
    background: var(--navy);
  }
  .front .accent-left {
    position: absolute; left: 0; top: 172px; width: 190px; height: 14px;
    background: var(--orange);
  }
  .front .wordmark {
    position: absolute; left: 70px; top: 48px;
    font-weight: 900; font-size: 64px; line-height: 1;
    color: var(--orange); letter-spacing: 1px;
    text-transform: uppercase;
  }
  .front .web {
    position: absolute; left: 150px; top: 218px;
    display: flex; align-items: center; gap: 14px;
    font-size: 15px; font-weight: 500; color: var(--ink);
  }
  .front .accent-right {
    position: absolute; right: 0; bottom: 18px; width: 200px; height: 14px;
    background: var(--orange);
  }
  .front .base {
    position: absolute; left: 0; bottom: 0; width: 100%; height: 18px;
    background: var(--white);
  }

  /* Back */
  .back { background: var(--paper); }
  .back .header {
    position: absolute; left: 0; top: 0; width: 100%; height: 72px;
    background: var(--navy);
  }
  .back .name-block {
    position: absolute; left: 40px; top: 16px; width: 200px; text-align: right;
    color: var(--white);
  }
  .back .name { font-size: 17px; font-weight: 700; letter-spacing: .5px; }
  .back .role { font-size: 12px; font-weight: 400; margin-top: 4px; }
  .back .header-accent {
    position: absolute; left: 0; top: 72px; width: 245px; height: 14px;
    background: var(--orange);
  }
  .back .wordmark {
    position: absolute; left: 34px; top: 116px;
    font-weight: 900; font-size: 38px; line-height: 1;
    color: var(--navy-deep); text-transform: uppercase;
  }
  .back .contact {
    position: absolute; left: 290px; top: 96px;
    list-style: none; display: flex; flex-direction: column; gap: 13px;
  }
  .back .contact li {
    display: flex; align-items: center; gap: 10px;
    font-size: 13px; color: var(--ink);
  }
  .back .contact .phone-row { margin-bottom: 12px; }
  .back .footer-accent {
    position: absolute; right: 0; bottom: 22px; width: 300px; height: 14px;
    background: var(--orange);
  }
  .back .footer {
    position: absolute; left: 0; bottom: 0; width: 100%; height: 22px;
    background: var(--navy);
  }

  .icon { width: 22px; height: 22px; flex: none; }
</style>
</head>
<body>

  <section class="card front" aria-label="Card front">
    <div class="dark-field"></div>
    <div class="accent-left"></div>
    <div class="wordmark">TRK Civil</div>
    <div class="web">
      <svg class="icon" viewBox="0 0 22 22" aria-hidden="true">
        <circle cx="11" cy="11" r="9" fill="var(--orange)"/>
        <g fill="none" stroke="#fff" stroke-width="1.1">
          <circle cx="11" cy="11" r="5"/>
          <ellipse cx="11" cy="11" rx="2.2" ry="5"/>
          <line x1="6" y1="11" x2="16" y2="11"/>
        </g>
      </svg>
      <span>www.trkcivil.com.au</span>
    </div>
    <div class="accent-right"></div>
    <div class="base"></div>
  </section>

  <section class="card back" aria-label="Card back">
    <div class="header"></div>
    <div class="name-block">
      <div class="name">Oliver Brantley</div>
      <div class="role">Director</div>
    </div>
    <div class="header-accent"></div>
    <div class="wordmark">TRK Civil</div>
    <ul class="contact">
      <li class="phone-row">
        <svg class="icon" viewBox="0 0 22 22" aria-hidden="true">
          <circle cx="11" cy="11" r="10" fill="var(--orange)"/>
          <path d="M7.5 6.5 L9.3 6.2 L10.2 8.6 L9 9.5 Q10 11.9 12.5 13 L13.4 11.8 L15.8 12.7 L15.5 14.5 Q11.5 15.5 8.6 12.4 Q6.3 9.8 7.5 6.5 Z" fill="#fff"/>
        </svg>
        <span>0461730582</span>
      </li>
      <li>
        <svg class="icon" viewBox="0 0 22 22" aria-hidden="true">
          <circle cx="11" cy="11" r="10" fill="var(--orange)"/>
          <rect x="6" y="7.5" width="10" height="7" fill="var(--navy)"/>
          <path d="M6 7.5 L11 11.5 L16 7.5" fill="none" stroke="#fff" stroke-width="1"/>
        </svg>
        <span>trkcivilworks@gmail.com</span>
      </li>
      <li>
        <svg class="icon" viewBox="0 0 22 22" aria-hidden="true">
          <circle cx="11" cy="11" r="10" fill="var(--orange)"/>
          <path d="M11 5.5 A3.8 3.8 0 0 1 14.8 9.3 C14.8 12 11 16.5 11 16.5 C11 16.5 7.2 12 7.2 9.3 A3.8 3.8 0 0 1 11 5.5 Z" fill="var(--navy)"/>
          <circle cx="11" cy="9.3" r="1.4" fill="#fff"/>
        </svg>
        <span>17 Wexcombe Rd Tarlow NSW 2291</span>
      </li>
      <li>
        <svg class="icon" viewBox="0 0 22 22" aria-hidden="true">
          <circle cx="11" cy="11" r="10" fill="var(--orange)"/>
          <rect x="7.5" y="5" width="7" height="12" rx="1.2" fill="none" stroke="var(--navy)" stroke-width="1.4"/>
          <line x1="10" y1="15" x2="12" y2="15" stroke="var(--navy)" stroke-width="1.2"/>
        </svg>
        <span>ABN: 52 308 917 465</span>
      </li>
    </ul>
    <div class="footer-accent"></div>
    <div class="footer"></div>
  </section>

</body>
</html>
```